Measures that matter

An internal dashboard of regular company results but with a twist!

No boring stats need apply- we want this to be visual and easy to digest for all staff on a monthly basis.

For instance, instead of a pie chat depicting the number of mobile projects won, make this a mobile charge icon ie 10 out of 50 = a fifth of charge. Or for churn rate of employees leaving the company, instead of a bar chart show 2 out of 10 people icons to show 20%.

This is built from a spreadsheet where formulas and pull throughs are already set so functionality needs to be intact.

There is one measure where there is a drop down filter, this should remain as a bar chart but be jazzed up as much as possible.

Branding elements and colours shown in the spreadsheet template, also attached is an example presentation so that you can gauge the brand tone.

Hoping for some awesome ideas here- let's show finance that design and marketing make a massive impact!

Reason: Really hoping for some clever ideas on this one so extending the deadline.

Hi Creative Minds! Really hoping to get your help on this project- a spreadsheet may seem daunting but it can be a really fun and visual project. Please let me know if you can help.

Marketing

• Century Gothic

```html
<!DOCTYPE html>
<html lang="en">
<head>
<meta charset="utf-8">
<title>Measures That Matter – APAC June 2014</title>
<link rel="stylesheet" href="https://fonts.googleapis.com/css2?family=Bebas+Neue&family=Questrial&display=swap">
<style>
  :root {
    --bg: #3f3f3f;
    --panel: #555555;
    --tube: #5e5e5e;
    --rule: #7a7a7a;
    --ink: #ffffff;
    --muted: #d6d6d6;
    --dark-ink: #2f2f2f;
    --orange: #f5923e;
    --green: #8dc63f;
    --blue: #8fd0e6;
    --grey-icon: #8a8a8a;
  }
  * { margin: 0; padding: 0; box-sizing: border-box; }
  html, body { width: 900px; height: 1200px; overflow: hidden; background: var(--bg); }
  body { font-family: "Questrial", "Century Gothic", sans-serif; color: var(--ink); }
  .dashboard { position: relative; width: 900px; height: 1200px; background: var(--bg); }
  .abs { position: absolute; }

  .title { left: 28px; top: 30px; font-family: "Bebas Neue", sans-serif; font-size: 54px; line-height: 1; letter-spacing: 1px; }
  .subtitle { left: 28px; top: 90px; font-family: "Bebas Neue", sans-serif; font-size: 27px; color: var(--orange); letter-spacing: 1px; }
  .brand { left: 666px; top: 46px; display: flex; align-items: center; gap: 8px; font-size: 20px; color: var(--ink); white-space: nowrap; }
  .brand-dot { width: 22px; height: 22px; border-radius: 50%; background: var(--orange); flex: none; }
  .header-rule { left: 28px; top: 129px; width: 843px; height: 1px; background: var(--rule); }

  .section-title { top: 165px; height: 47px; border-top: 1px solid var(--rule); border-bottom: 1px solid var(--rule);
    font-family: "Bebas Neue", sans-serif; font-size: 38px; line-height: 47px; letter-spacing: 1px; padding-left: 2px; white-space: nowrap; }
  .pocket-title { left: 52px; width: 160px; color: var(--orange); }
  .engine-title { left: 318px; width: 255px; color: var(--green); }
  .chosen-title { left: 620px; width: 225px; color: var(--blue); }

  .ribbon { height: 30px; line-height: 30px; text-align: center; font-weight: 700; font-size: 12.5px;
    color: var(--dark-ink); letter-spacing: 0.3px; text-transform: uppercase; white-space: nowrap;
    clip-path: polygon(0 0, calc(100% - 11px) 0, 100% 50%, calc(100% - 11px) 100%, 0 100%); }
  .ribbon-orange { background: var(--orange); left: 22px; width: 238px; }
  .ribbon-green { background: var(--green); left: 288px; width: 302px; }
  .ribbon-blue { background: var(--blue); left: 620px; width: 248px; }

  .select-box { left: 146px; width: 85px; height: 19px; background: var(--panel); color: var(--muted);
    font-size: 11px; line-height: 19px; text-align: center; }
  .bar-chart { left: 22px; }
  .total-row { left: 22px; width: 238px; height: 25px; background: var(--panel); font-size: 11px; line-height: 25px; }
  .total-row span { position: absolute; top: 0; color: var(--orange); }
  .total-row .total-label { left: 0; font-size: 9.5px; }
  .total-row .total-value { color: #e8a872; font-weight: 700; transform: translateX(-50%); }

  .profit-value { left: 50px; font-family: "Bebas Neue", sans-serif; font-size: 46px; line-height: 1; }
  .profit-money { color: var(--orange); top: 995px; }
  .profit-pct { color: var(--ink); top: 1048px; }
  .cash-stack { left: 156px; top: 981px; width: 100px; height: 119px;
    background: linear-gradient(180deg, #9a9a9a 0%, #8a8a8a 35%, var(--orange) 36%, #c9772f 100%); }

  .big-figure { font-family: "Bebas Neue", sans-serif; color: var(--green); line-height: 1; white-space: nowrap; }
  .ftr-score { left: 481px; top: 296px; font-size: 72px; }
  .caption { left: 288px; width: 302px; text-align: center; font-size: 12px; color: var(--ink); text-transform: uppercase; white-space: nowrap; }
  .mobile-count { left: 296px; top: 786px; font-size: 56px; }
</style>
</head>
<body>
<main class="dashboard">

  <h1 class="abs title">Measures That Matter</h1>
  <p class="abs subtitle">APAC – June 2014</p>
  <div class="abs brand"><span class="brand-dot"></span>Northgate Research</div>
  <div class="abs header-rule"></div>

  <!-- Finance column -->
  <h2 class="abs section-title pocket-title">The Pocket</h2>

  <div class="abs ribbon ribbon-orange" style="top:228px">Revenue vs Target</div>
  <div class="abs select-box" style="top:266px">Select a BU</div>
  <div class="abs select-box" style="top:289px">Total APAC</div>
  <svg class="abs bar-chart" style="top:318px" width="240" height="200" viewBox="0 0 240 200">
    <defs>
      <pattern id="hatch" width="7" height="7" patternUnits="userSpaceOnUse" patternTransform="rotate(45)">
        <rect width="7" height="7" fill="#c47a38"/>
        <rect width="3.5" height="7" fill="#f5a25a"/>
      </pattern>
      <clipPath id="tube-a"><rect x="75" y="9" width="29" height="163" rx="14.5"/></clipPath>
      <clipPath id="tube-b"><rect x="130" y="9" width="29" height="163" rx="14.5"/></clipPath>
      <clipPath id="tube-c"><rect x="187" y="9" width="29" height="163" rx="14.5"/></clipPath>
    </defs>
    <g fill="#ffffff" font-size="8" text-anchor="middle" font-family="Questrial, sans-serif">
      <text x="32" y="20">900</text><text x="32" y="39">800</text><text x="32" y="58">700</text>
      <text x="32" y="76">600</text><text x="32" y="95">500</text><text x="32" y="114">400</text>
      <text x="32" y="133">300</text><text x="32" y="151">200</text><text x="32" y="170">100</text>
      <text x="28" y="189">-</text>
    </g>
    <rect x="75" y="9" width="29" height="163" rx="14.5" fill="var(--tube)"/>
    <rect x="130" y="9" width="29" height="163" rx="14.5" fill="var(--tube)"/>
    <rect x="187" y="9" width="29" height="163" rx="14.5" fill="var(--tube)"/>
    <rect x="75" y="62" width="29" height="110" fill="url(#hatch)" clip-path="url(#tube-a)"/>
    <rect x="130" y="26" width="29" height="146" fill="url(#hatch)" clip-path="url(#tube-b)"/>
    <rect x="187" y="143" width="29" height="29" fill="url(#hatch)" clip-path="url(#tube-c)"/>
    <g fill="#ffffff" font-size="7.5" font-family="Questrial, sans-serif">
      <text x="75" y="184">MTD</text><text x="75" y="193">Variance</text>
      <text x="130" y="184">YTD</text><text x="130" y="193">Variance</text>
      <text x="187" y="184">FY Q2RF</text>
    </g>
  </svg>
  <div class="abs total-row" style="top:528px">
    <span class="total-label">Total APAC</span>
    <span class="total-value" style="left:89px">609</span>
    <span class="total-value" style="left:144px">804</span>
    <span class="total-value" style="left:201px">134</span>
  </div>

  <div class="abs ribbon ribbon-orange" style="top:581px">Sales vs Target</div>
  <div class="abs select-box" style="top:619px">Select a BU</div>
  <div class="abs select-box" style="top:642px">Total APAC</div>
  <svg class="abs bar-chart" style="top:671px" width="240" height="200" viewBox="0 0 240 200">
    <defs>
      <clipPath id="tube-d"><rect x="75" y="9" width="29" height="163" rx="14.5"/></clipPath>
      <clipPath id="tube-e"><rect x="130" y="9" width="29" height="163" rx="14.5"/></clipPath>
      <clipPath id="tube-f"><rect x="187" y="9" width="29" height="163" rx="14.5"/></clipPath>
    </defs>
    <g fill="#ffffff" font-size="8" text-anchor="middle" font-family="Questrial, sans-serif">
      <text x="32" y="20">900</text><text x="32" y="39">800</text><text x="32" y="58">700</text>
      <text x="32" y="76">600</text><text x="32" y="95">500</text><text x="32" y="114">400</text>
      <text x="32" y="133">300</text><text x="32" y="151">200</text><text x="32" y="170">100</text>
      <text x="28" y="189">-</text>
    </g>
    <rect x="75" y="9" width="29" height="163" rx="14.5" fill="var(--tube)"/>
    <rect x="130" y="9" width="29" height="163" rx="14.5" fill="var(--tube)"/>
    <rect x="187" y="9" width="29" height="163" rx="14.5" fill="var(--tube)"/>
    <rect x="75" y="62" width="29" height="110" fill="url(#hatch)" clip-path="url(#tube-d)"/>
    <rect x="130" y="26" width="29" height="146" fill="url(#hatch)" clip-path="url(#tube-e)"/>
    <rect x="187" y="143" width="29" height="29" fill="url(#hatch)" clip-path="url(#tube-f)"/>
    <g fill="#ffffff" font-size="7.5" font-family="Questrial, sans-serif">
      <text x="75" y="184">MTD</text><text x="75" y="193">Variance</text>
      <text x="130" y="184">YTD</text><text x="130" y="193">Variance</text>
      <text x="187" y="184">FY Q2RF</text>
    </g>
  </svg>
  <div class="abs total-row" style="top:881px">
    <span class="total-label">Total APAC</span>
    <span class="total-value" style="left:89px">609</span>
    <span class="total-value" style="left:144px">804</span>
    <span class="total-value" style="left:201px">134</span>
  </div>

  <div class="abs ribbon ribbon-orange" style="top:938px">Operating Profit vs Target</div>
  <p class="abs profit-value profit-money">-1.8M</p>
  <p class="abs profit-value profit-pct">-31%</p>
  <div class="abs cash-stack" role="img" aria-label="Stack of banknotes"></div>

  <!-- Operations column -->
  <h2 class="abs section-title engine-title">The Engine Room</h2>

  <div class="abs ribbon ribbon-green" style="top:228px">First Time Right Scores (AU Only)</div>
  <svg class="abs" style="left:290px;top:280px" width="150" height="120" viewBox="0 0 150 120">
    <defs>
      <g id="tick-on"><circle r="10" fill="var(--green)"/><path d="M-5 0 L-1.5 4 L5.5 -4" fill="none" stroke="#3f3f3f" stroke-width="2.6" stroke-linecap="round" stroke-linejoin="round"/></g>
      <g id="tick-off"><circle r="10" fill="var(--grey-icon)"/><path d="M-5 0 L-1.5 4 L5.5 -4" fill="none" stroke="#3f3f3f" stroke-width="2.6" stroke-linecap="round" stroke-linejoin="round"/></g>
    </defs>
    <use href="#tick-on" x="16" y="16"/><use href="#tick-on" x="45" y="16"/><use href="#tick-on" x="74" y="16"/><use href="#tick-on" x="103" y="16"/><use href="#tick-on" x="132" y="16"/>
    <use href="#tick-on" x="16" y="45"/><use href="#tick-on" x="45" y="45"/><use href="#tick-on" x="74" y="45"/><use href="#tick-on" x="103" y="45"/><use href="#tick-on" x="132" y="45"/>
    <use href="#tick-off" x="16" y="74"/><use href="#tick-off" x="45" y="74"/><use href="#tick-off" x="74" y="74"/><use href="#tick-off" x="103" y="74"/><use href="#tick-off" x="132" y="74"/>
    <use href="#tick-off" x="16" y="103"/><use href="#tick-off" x="45" y="103"/><use href="#tick-off" x="74" y="103"/><use href="#tick-off" x="103" y="103"/><use href="#tick-off" x="132" y="103"/>
  </svg>
  <p class="abs big-figure ftr-score">50%</p>

  <div class="abs ribbon ribbon-green" style="top:415px">Panel Partner Spend</div>
  <svg class="abs" style="left:288px;top:455px" width="302" height="215" viewBox="0 0 302 215">
    <g fill="#ffffff" font-size="8" text-anchor="end" font-family="Questrial, sans-serif">
      <text x="30" y="11">300</text><text x="30" y="38">250</text><text x="30" y="64">200</text>
      <text x="30" y="91">150</text><text x="30" y="118">100</text><text x="30" y="144">50</text><text x="30" y="171">0</text>
    </g>
    <path d="M36 8 V168 H296" fill="none" stroke="#9a9a9a" stroke-width="1"/>
    <polyline fill="none" stroke="var(--green)" stroke-width="2"
      points="40,21 61,112 82,117 103,93 123,99 144,112 165,112 186,108 207,133 228,135 248,149 269,107 290,158"/>
    <g fill="var(--green)" stroke="#6e9a30" stroke-width="1">
      <circle cx="40" cy="21" r="4.5"/><circle cx="61" cy="112" r="4.5"/><circle cx="82" cy="117" r="4.5"/>
      <circle cx="103" cy="93" r="4.5"/><circle cx="123" cy="99" r="4.5"/><circle cx="144" cy="112" r="4.5"/>
      <circle cx="165" cy="112" r="4.5"/><circle cx="186" cy="108" r="4.5"/><circle cx="207" cy="133" r="4.5"/>
      <circle cx="228" cy="135" r="4.5"/><circle cx="248" cy="149" r="4.5"/><circle cx="269" cy="107" r="4.5"/>
      <circle cx="290" cy="158" r="4.5"/>
    </g>
    <g fill="#ffffff" font-size="7.5" text-anchor="end" font-family="Questrial, sans-serif">
      <text transform="translate(44 178) rotate(-45)">Jun-13</text>
      <text transform="translate(65 178) rotate(-45)">Jul-13</text>
      <text transform="translate(86 178) rotate(-45)">Aug-13</text>
      <text transform="translate(107 178) rotate(-45)">Sep-13</text>
      <text transform="translate(127 178) rotate(-45)">Oct-13</text>
      <text transform="translate(148 178) rotate(-45)">Nov-13</text>
      <text transform="translate(169 178) rotate(-45)">Dec-13</text>
      <text transform="translate(190 178) rotate(-45)">Jan-14</text>
      <text transform="translate(211 178) rotate(-45)">Feb-14</text>
      <text transform="translate(232 178) rotate(-45)">Mar-14</text>
      <text transform="translate(252 178) rotate(-45)">Apr-14</text>
      <text transform="translate(273 178) rotate(-45)">May-14</text>
      <text transform="translate(294 178) rotate(-45)">Jun-14</text>
    </g>
  </svg>

  <div class="abs ribbon ribbon-green" style="top:688px">The Classifieds</div>
  <p class="abs caption" style="top:732px"># Mobile Studies vs Annual Target</p>
  <p class="abs big-figure mobile-count">11/50</p>
  <svg class="abs" style="left:414px;top:778px" width="174" height="64" viewBox="0 0 174 64">
    <rect x="2" y="2" width="160" height="60" rx="7" fill="none" stroke="#9a9a9a" stroke-width="4"/>
    <rect x="164" y="20" width="8" height="24" rx="2" fill="#9a9a9a"/>
    <rect x="12" y="12" width="9" height="40" fill="var(--green)"/>
    <rect x="24" y="12" width="9" height="40" fill="var(--green)"/>
    <rect x="36" y="12" width="9" height="40" fill="var(--green)"/>
  </svg>

  <div class="abs ribbon ribbon-green" style="top:879px">The Tribe</div>
  <p class="abs caption" style="top:923px">Employee Turnover Rate</p>
  <svg class="abs" style="left:294px;top:960px" width="296" height="60" viewBox="0 0 296 60">
    <defs>
      <g id="person">
        <circle cx="12" cy="6" r="6"/>
        <path d="M3 14 H21 Q24 14 24 17 V34 H20 V58 H14 V36 H10 V58 H4 V34 H0 V17 Q0 14 3 14 Z"/>
      </g>
    </defs>
    <g fill="var(--green)">
      <use href="#person" x="2"/><use href="#person" x="31"/><use href="#person" x="60"/><use href="#person" x="89"/>
    </g>
    <g fill="var(--grey-icon)">
      <use href="#person" x="118"/><use href="#person" x="147"/><use href="#person" x="176"/>
      <use href="#person" x="205"/><use href="#person" x="234"/><use href="#person" x="263"/>
    </g>
  </svg>
  <p class="abs caption" style="top:1028px">APAC 12 Month Rolling Churn Rate</p>

  <div class="abs ribbon ribbon-green" style="top:1073px">Average Annual Leave Days (AU Only)</div>

  <!-- Client column -->
  <h2 class="abs section-title chosen-title">The Chosen Ones</h2>

  <div class="abs ribbon ribbon-blue" style="top:228px">Average CSAT Result (YTD)</div>
  <svg class="abs" style="left:620px;top:266px" width="250" height="240" viewBox="0 0 250 240">
    <defs>
      <g id="callout">
        <rect x="-17" y="0" width="34" height="24" fill="var(--blue)"/>
        <path d="M-5 24 L0 31 L5 24 Z" fill="var(--blue)"/>
      </g>
      <g id="note" fill="none" stroke-width="2.2" stroke-linejoin="round" stroke-linecap="round">
        <path d="M-9 -6 H-3 M-9 -6 V10 H7 V4"/>
        <path d="M-2 4 L-1 -1 L8 -10 L12 -6 L3 3 Z"/>
      </g>
    </defs>
    <use href="#callout" x="46" y="2"/><use href="#callout" x="90" y="2"/><use href="#callout" x="134" y="2"/>
    <use href="#callout" x="178" y="2"/><use href="#callout" x="223" y="2"/>
    <g fill="var(--dark-ink)" font-size="13" font-weight="700" text-anchor="middle" font-family="Questrial, sans-serif">
      <text x="46" y="19">6.0</text><text x="90" y="19">8.1</text><text x="134" y="19">8.2</text>
      <text x="178" y="19">8.0</text><text x="223" y="19">9.0</text>
    </g>
    <g fill="#ffffff" font-size="8" font-family="Questrial, sans-serif">
      <text x="2" y="56">10</text><text x="4" y="71">9</text><text x="4" y="89">8</text><text x="4" y="105">7</text>
      <text x="4" y="122">6</text><text x="4" y="140">5</text><text x="4" y="156">4</text><text x="4" y="174">3</text>
      <text x="4" y="191">2</text><text x="4" y="208">1</text><text x="4" y="224">-</text>
    </g>
    <g stroke="var(--grey-icon)">
      <use href="#note" x="46" y="60"/><use href="#note" x="46" y="97"/>
      <use href="#note" x="90" y="60"/><use href="#note" x="134" y="60"/><use href="#note" x="178" y="60"/>
    </g>
    <g stroke="var(--blue)">
      <use href="#note" x="46" y="134"/><use href="#note" x="46" y="170"/><use href="#note" x="46" y="206"/>
      <use href="#note" x="90" y="97"/><use href="#note" x="90" y="134"/><use href="#note" x="90" y="170"/><use href="#note" x="90" y="206"/>
      <use href="#note" x="134" y="97"/><use href="#note" x="134" y="134"/><use href="#note" x="134" y="170"/><use href="#note" x="134" y="206"/>
      <use href="#note" x="178" y="97"/><use href="#note" x="178" y="134"/><use href="#note" x="178" y="170"/><use href="#note" x="178" y="206"/>
      <use href="#note" x="223" y="60"/><use href="#note" x="223" y="97"/><use href="#note" x="223" y="134"/><use href="#note" x="223" y="170"/><use href="#note" x="223" y="206"/>
    </g>
    <g fill="var(--orange)" font-size="10" font-weight="700" text-anchor="middle" font-family="Questrial, sans-serif">
      <text x="46" y="236">XX</text><text x="90" y="236">XX</text><text x="134" y="236">XX</text>
      <text x="178" y="236">XX</text><text x="223" y="236">XX</text>
    </g>
  </svg>

  <div class="abs ribbon ribbon-blue" style="top:529px">APAC Client Analysis (YTD)</div>

</main>
</body>
</html>
```